TULVAN COFFEE Menu Re-Design (drive-thru coffee shop)

* Keep style of old menu and fonts

* Change to new layout with orange outlines around each product section. I want the orange outlines to look like the orange circle around the "tax not included" on the old menu. I've attached "NEW menu layout 1" for reference.

* Change to new layout, products, sizes, and prices. I attached "Tulvan Menu NEW" for reference.

* Change background color of menu from dark blue to light/medium grey

* Change to new logo (my attachment has 3 logos. Use the top/1st logo please).

Let me know if there are any questions about anything or if you need different file types.

Thank you!

Industry/Entity Type

Coffee

Font styles to use
Other font styles liked:
• High Voltage (I've attached the font in the brief.)

Colors
F0912C
F2A743
F7CA91
FBE8D2
FDF5EE

Requirements
Must have
• Grey, Orange and White theme.
Should not have
• The color black

```html
<!DOCTYPE html>
<html lang="en">
<head>
<meta charset="utf-8">
<title>Tulvan Coffee Menu</title>
<link href="https://fonts.googleapis.com/css2?family=Anton&family=Oswald:wght@400;500;600&display=swap" rel="stylesheet">
<style>
:root{
  --backdrop:#d6cfcd;
  --paper:#e8e9ea;
  --flame:#f0512a;
  --frame:#f0912c;
  --grey:#808184;
  --ink:#3d3d40;
  --white:#fdf5ee;
}
*{box-sizing:border-box;margin:0;padding:0}
html,body{width:1200px;height:800px;overflow:hidden;background:var(--backdrop)}
.canvas{position:relative;width:1200px;height:800px}
.sheet{position:absolute;width:412px;height:686px;background:var(--paper);top:57px}
.sheet--cover{left:171px}
.sheet--menu{left:616px}
.sheet *{position:absolute}
.frame{left:18px;top:18px;width:380px;height:652px;border:1.5px solid var(--frame)}
.frame::after{content:"";position:absolute;left:-6px;top:-6px;right:-6px;bottom:-6px;border:1px solid var(--frame);opacity:.7}
.dot{width:8px;height:8px;border-radius:50%;background:var(--frame)}

/* cover */
.brand-dot{left:181px;top:150px;width:50px;height:50px;border-radius:50%;background:var(--grey)}
.brand{left:0;width:412px;text-align:center;font-family:"Anton",sans-serif;color:var(--flame);line-height:1}
.brand--name{top:225px;font-size:100px;letter-spacing:2px}
.brand--sub{top:348px;font-size:34px;letter-spacing:10px}
.contact{left:0;width:412px;text-align:center;color:var(--flame);font-family:"Anton",sans-serif;line-height:1}
.contact--phone{top:550px;font-size:30px;letter-spacing:1px}
.contact--street{top:590px;font-family:"Oswald",sans-serif;font-weight:600;font-size:19px}
.contact--web{top:616px;font-family:"Oswald",sans-serif;font-weight:600;font-size:17px}

/* menu */
.menu-brand{left:130px;width:132px;text-align:center;font-family:"Anton",sans-serif;color:var(--flame);line-height:1}
.menu-brand--name{top:80px;font-size:38px}
.menu-brand--sub{top:122px;font-size:12px;letter-spacing:4px}
.menu-brand-dot{left:187px;top:56px;width:18px;height:18px;border-radius:50%;background:var(--grey)}

.badge{display:flex;align-items:center;justify-content:center;text-align:center;font-family:"Oswald",sans-serif;font-weight:600;font-size:7px;line-height:1;color:var(--ink);height:24px}
.badge::before{content:"";position:absolute;inset:0;border:2px solid var(--flame);border-radius:50%;transform:rotate(-4deg)}
.badge span{position:relative}

.banner{background:var(--flame);color:var(--white);font-family:"Anton",sans-serif;text-align:center;line-height:1;display:flex;align-items:center;justify-content:center}

.list{font-family:"Oswald",sans-serif;font-weight:500;font-size:5.2px;line-height:7.3px;color:var(--ink);letter-spacing:.3px;white-space:nowrap}
.list p{position:static}
.list small{position:static;font-size:3.2px;letter-spacing:.1px}
.prices{display:grid;font-family:"Oswald",sans-serif;font-weight:500;font-size:5.4px;line-height:7.3px;color:var(--ink);white-space:nowrap}
.prices *{position:static}
.sizes{display:grid;font-family:"Oswald",sans-serif;font-size:2.4px;line-height:3px;color:var(--flame);white-space:nowrap}
.sizes *{position:static}
.note{font-family:"Oswald",sans-serif;font-weight:500;font-size:4.6px;color:var(--ink);white-space:nowrap}

.flavor-box{left:35px;top:241px;width:340px;height:67px;border:1.5px solid var(--frame)}
.flavor{width:100px;text-align:center}
.flavor h3{position:static;font-family:"Oswald",sans-serif;font-weight:500;font-size:6.5px;color:var(--flame);letter-spacing:.5px}
.flavor p{position:static;margin-top:4px;font-family:"Oswald",sans-serif;font-size:4.4px;line-height:7.5px;color:var(--ink)}
</style>
</head>
<body>
<div class="canvas">

  <section class="sheet sheet--cover">
    <div class="frame"></div>
    <div class="dot" style="left:14px;top:14px"></div>
    <div class="dot" style="left:390px;top:14px"></div>
    <div class="dot" style="left:14px;top:664px"></div>
    <div class="dot" style="left:390px;top:664px"></div>

    <div class="brand-dot"></div>
    <h1 class="brand brand--name">TULVAN</h1>
    <p class="brand brand--sub">COFFEE</p>

    <p class="contact contact--phone">000 1234 56</p>
    <p class="contact contact--street">Street Address, nº20</p>
    <p class="contact contact--web">www.companyname.com</p>
  </section>

  <section class="sheet sheet--menu">
    <div class="frame"></div>
    <div class="dot" style="left:14px;top:14px"></div>
    <div class="dot" style="left:390px;top:14px"></div>
    <div class="dot" style="left:14px;top:664px"></div>
    <div class="dot" style="left:390px;top:664px"></div>

    <div class="menu-brand-dot"></div>
    <h1 class="menu-brand menu-brand--name">TULVAN</h1>
    <p class="menu-brand menu-brand--sub">COFFEE</p>

    <!-- espresso -->
    <div class="badge" style="left:53px;top:46px;width:48px"><span>ESPRESSO</span></div>
    <div class="list" style="left:34px;top:72px"><p>HOT | ICED</p></div>
    <div class="list" style="left:34px;top:80px"><p>LATTE</p><p>BREVE</p><p>MACCHIATO</p><p>CAPPUCINO</p><p>AMERICANO</p><p>ESPRESSO</p></div>
    <div class="prices" style="left:71px;top:80px;grid-template-columns:19px 19px 19px">
      <span>$3.95</span><span>$4.45</span><span>$5.45</span>
      <span>$3.95</span><span>$4.45</span><span>$5.45</span>
      <span>$3.95</span><span>$4.45</span><span>$5.45</span>
      <span>$3.70</span><span>$4.20</span><span>$5.20</span>
      <span>$2.45</span><span>$2.95</span><span>$3.95</span>
      <span>$1.50</span>
    </div>

    <!-- frozen espresso -->
    <div class="badge" style="left:293px;top:46px;width:68px"><span>FROZEN ESPRESSO</span></div>
    <div class="list" style="left:270px;top:80px"><p>MOCHA</p><p>WHITE CHOCOLATE</p><p>CARAMEL MELTDOWN</p><p>MINT CHOCOLATE CHIP</p><p>COOKIE CRUMBLE</p><p>BUTTER CRUNCH</p><p>PEANUT CUP</p><p>ALMOND BLISS</p><p>NSA VANILLA BEAN</p><p>NSA MOCHA</p></div>
    <div class="sizes" style="left:327px;top:81px;grid-template-columns:18px 18px 18px"><span>SMALL</span><span>MEDIUM</span><span>LARGE</span></div>
    <div class="prices" style="left:327px;top:86px;grid-template-columns:18px 18px 18px"><span>$4.75</span><span>$5.75</span><span>$6.75</span></div>

    <!-- cold brew -->
    <div class="badge" style="left:43px;top:152px;width:68px;height:28px"><span>COLD BREW -<br>NITRO COLD BREW</span></div>
    <div class="note" style="left:34px;top:186px">ADD ANY FLAVOR | ADD COLD FOAM +.50</div>
    <div class="sizes" style="left:71px;top:200px;grid-template-columns:19px 19px 19px"><span>SMALL</span><span>MEDIUM</span><span>LARGE</span></div>
    <div class="list" style="left:34px;top:205px"><p>COLD BREW</p></div>
    <div class="prices" style="left:71px;top:205px;grid-template-columns:19px 19px 19px"><span>$3.75</span><span>$4.25</span><span>$4.75</span></div>

    <!-- drip coffee -->
    <div class="badge" style="left:179px;top:155px;width:48px"><span>DRIP COFFEE</span></div>
    <div class="sizes" style="left:190px;top:188px;grid-template-columns:19px 19px 19px"><span>SMALL</span><span>MEDIUM</span><span>LARGE</span></div>
    <div class="list" style="left:152px;top:193px"><p>DRIP COFFEE</p></div>
    <div class="prices" style="left:190px;top:193px;grid-template-columns:19px 19px 19px"><span>$1.75</span><span>$2.25</span><span>$2.75</span></div>

    <!-- dairy free -->
    <div class="badge" style="left:298px;top:156px;width:66px;height:26px"><span>DAIRY FREE<br>ADD-ON'S</span></div>
    <div class="list" style="left:270px;top:190px"><p>ALMOND</p><p>SOY</p><p>OAT</p><p>COCONUT</p><p>ESPRESSO SHOT | $.50</p><p>EXTRA FLAVOR | FREE</p></div>
    <div class="list" style="left:331px;top:190px"><p>WHIPPED CREAM</p><p>| FREE</p><p>SWEET CREAM</p><p>COLD FOAM | $.50</p></div>

    <!-- flavors -->
    <div class="flavor-box"></div>
    <div class="banner" style="left:156px;top:227px;width:102px;height:29px;font-size:20px">FLAVORS</div>
    <div class="flavor" style="left:50px;top:268px"><h3>LOREM IPSUM</h3><p>Lorem ipsum dolor sit amet, consecte<br>adipelit, sed diam nibh.</p></div>
    <div class="flavor" style="left:152px;top:268px"><h3>LOREM IPSUM</h3><p>Lorem ipsum dolor sit amet, consecte<br>adipelit, sed diam nibh.</p></div>
    <div class="flavor" style="left:256px;top:268px"><h3>LOREM IPSUM</h3><p>Lorem ipsum dolor sit amet, consecte<br>adipelit, sed diam nibh.</p></div>

    <!-- tea -->
    <div class="banner" style="left:182px;top:315px;width:51px;height:22px;font-size:17px">TEA</div>

    <div class="badge" style="left:60px;top:345px;width:46px"><span>CHAI</span></div>
    <div class="note" style="left:34px;top:376px">HOT | ICED +$.50 | FROZEN +$1</div>
    <div class="list" style="left:34px;top:390px"><p>SPICED</p><p>CHOCOLATE</p><p>RASPBERRY</p></div>
    <div class="list" style="left:69px;top:390px"><p>VANILLA</p><p>NSA VANILLA</p></div>
    <div class="sizes" style="left:102px;top:385px;grid-template-columns:17px 17px 17px"><span>SMALL</span><span>MEDIUM</span><span>LARGE</span></div>
    <div class="prices" style="left:102px;top:390px;grid-template-columns:17px 17px 17px"><span>$3.75</span><span>$4.50</span><span>$5.50</span></div>

    <div class="badge" style="left:185px;top:345px;width:48px"><span>HOT TEA</span></div>
    <div class="list" style="left:158px;top:375px"><p>ENGLISH BREAKFAST</p><p>EARL GREY</p><p>SWEET CINNAMON</p><p>CAPPUCINO</p><p>GREEN TEA</p></div>
    <div class="list" style="left:212px;top:375px"><p>MINT</p><p>PEACH</p></div>
    <div class="sizes" style="left:231px;top:370px;grid-template-columns:18px 18px 18px"><span>SMALL</span><span>MEDIUM</span><span>LARGE</span></div>
    <div class="prices" style="left:231px;top:375px;grid-template-columns:18px 18px 18px"><span>$2.25</span><span>$2.75</span><span>$2.95</span></div>

    <div class="badge" style="left:317px;top:345px;width:47px"><span>ICED TEA</span></div>
    <div class="note" style="left:289px;top:376px">ADD ANY FLAVOR</div>
    <div class="list" style="left:289px;top:390px"><p>BLACK TEA</p><p>GREEN TEA</p></div>
    <div class="sizes" style="left:327px;top:386px;grid-template-columns:18px 18px 18px"><span>SMALL</span><span>MEDIUM</span><span>LARGE</span></div>
    <div class="prices" style="left:327px;top:391px;grid-template-columns:18px 18px 18px"><span>$2.95</span><span>$3.25</span><span>$3.50</span></div>

    <!-- energy sodas -->
    <div class="banner" style="left:131px;top:416px;width:168px;height:30px;font-size:16px;letter-spacing:.5px">TULVAN ENERGY SODA'S</div>

    <div class="badge" style="left:60px;top:457px;width:46px"><span>RED BOLT</span></div>
    <div class="note" style="left:34px;top:484px">ICED | FROZEN</div>
    <div class="sizes" style="left:71px;top:490px;grid-template-columns:19px 19px"><span>SMALL</span><span>LARGE</span></div>
    <div class="list" style="left:34px;top:495px"><p>RED BOLT</p></div>
    <div class="prices" style="left:71px;top:495px;grid-template-columns:19px 19px"><span>$5.95</span><span>$7.95</span></div>

    <div class="badge" style="left:170px;top:457px;width:82px"><span>LUMEN PLANT ENERGY</span></div>
    <div class="note" style="left:171px;top:490px">ICED | FROZEN</div>
    <div class="sizes" style="left:210px;top:497px;grid-template-columns:19px 19px"><span>SMALL</span><span>LARGE</span></div>
    <div class="list" style="left:171px;top:502px"><p>LUMEN</p></div>
    <div class="prices" style="left:210px;top:502px;grid-template-columns:19px 19px"><span>$5.75</span><span>$6.75</span></div>

    <div class="badge" style="left:318px;top:457px;width:46px"><span>FROZEN</span></div>
    <div class="note" style="left:307px;top:490px">ICED | FROZEN</div>
    <div class="sizes" style="left:344px;top:497px;grid-template-columns:19px 19px"><span>SMALL</span><span>LARGE</span></div>
    <div class="list" style="left:307px;top:502px"><p>FROZEN</p></div>
    <div class="prices" style="left:344px;top:502px;grid-template-columns:19px 19px"><span>$5.75</span><span>$6.75</span></div>

    <!-- smoothies & lemonade -->
    <div class="badge" style="left:48px;top:521px;width:92px;height:28px"><span>PUREFRUIT SMOOTHIES</span></div>
    <div class="list" style="left:34px;top:560px"><p>STRAWBERRY</p><p>STRAWBERRY BANANA</p><p>PEACH</p></div>
    <div class="list" style="left:101px;top:560px"><p>MANGO</p><p>SUPERFRUIT</p><p>TROPICAL</p></div>
    <div class="sizes" style="left:142px;top:556px;grid-template-columns:19px 19px 19px"><span>SMALL</span><span>MEDIUM</span><span>LARGE</span></div>
    <div class="prices" style="left:142px;top:561px;grid-template-columns:19px 19px 19px"><span>$5.75</span><span>$6.75</span><span>$7.75</span></div>

    <div class="badge" style="left:283px;top:521px;width:92px;height:28px"><span>HANDCRAFTED LEMONADE</span></div>
    <div class="list" style="left:226px;top:560px"><p>ORIGINAL</p><p>BLUE RASPBERRY</p><p>BLACKBERRY</p></div>
    <div class="list" style="left:282px;top:560px"><p>STRAWBERRY</p><p>PEACH</p><p>CHERRY</p></div>
    <div class="sizes" style="left:327px;top:556px;grid-template-columns:19px 19px 19px"><span>SMALL</span><span>MEDIUM</span><span>LARGE</span></div>
    <div class="prices" style="left:327px;top:561px;grid-template-columns:19px 19px 19px"><span>$5.75</span><span>$6.75</span><span>$7.75</span></div>

    <!-- hot chocolate / italian sodas / kids -->
    <div class="badge" style="left:43px;top:587px;width:80px;height:28px"><span>HOT CHOCOLATE</span></div>
    <div class="note" style="left:35px;top:626px">TRY A "FROZEN" HOT CHOCOLATE +$.50</div>
    <div class="sizes" style="left:82px;top:636px;grid-template-columns:19px 19px 19px"><span>SMALL</span><span>MEDIUM</span><span>LARGE</span></div>
    <div class="list" style="left:34px;top:640px"><p>ADD ANY FLAVOR</p></div>
    <div class="prices" style="left:82px;top:640px;grid-template-columns:19px 19px 19px"><span>$2.75</span><span>$3.25</span><span>$3.75</span></div>

    <div class="badge" style="left:158px;top:587px;width:80px;height:28px"><span>ITALIAN SODAS</span></div>
    <div class="note" style="left:144px;top:626px">(INFUSE WITH ANY FLAVORS)</div>
    <div class="list" style="left:144px;top:640px"><p>WITH OR WITHOUT CREAM</p></div>
    <div class="sizes" style="left:213px;top:636px;grid-template-columns:19px 19px 19px"><span>SMALL</span><span>MEDIUM</span><span>LARGE</span></div>
    <div class="prices" style="left:213px;top:640px;grid-template-columns:19px 19px 19px"><span>$2.95</span><span>$3.45</span><span>$3.95</span></div>

    <div class="badge" style="left:289px;top:587px;width:80px;height:28px"><span>KIDS</span></div>
    <div class="note" style="left:272px;top:623px;font-size:3.8px">ALL DRINKS COME WITH WHIP CREAM AND SPRINKLES</div>
    <div class="list" style="left:272px;top:632px"><p>PUREFRUIT SMOOTHIE | <small>ANY FLAVOR</small></p><p>STEAMER | <small>ANY FLAVOR + WARM STEAMED MILK</small></p></div>
    <div class="prices" style="left:365px;top:632px;grid-template-columns:19px"><span>$3.95</span><span>$2.25</span></div>
  </section>

</div>
</body>
</html>
```